FixyNestly.com Needs a new Design

We need a card design for a new start up company in the Sacramento Ca area called FixyNestly.com. We offer homeowners three levels of yearly home maintenance memberships that will help them take care of their yearly home maintenance needs even if there on a fixed income.
Our company tag line is ( We Tackle The Chore Lists That Other Crews Skip Past! )
Updates

Information to be put on card. Carl Wenstow Director Phone: 800-537-2916 Fax: 800-537-2916 Address: 4826 Birch Ln Pellford CA 95712

Industry/Entity Type

It Company

```html
<!DOCTYPE html>
<html lang="en">
<head>
<meta charset="utf-8">
<title>FixyNestly.com – Logo and Business Card</title>
<link href="https://fonts.googleapis.com/css2?family=Open+Sans:wght@400;600;800&display=swap" rel="stylesheet">
<style>
  :root {
    --ink: #262626;
    --charcoal: #333335;
    --charcoal-light: #48484b;
    --orange: #e8671c;
    --paper: #ffffff;
    --backdrop: #ecebe8;
  }
  * { box-sizing: border-box; margin: 0; padding: 0; }
  html, body { width: 1200px; height: 1000px; overflow: hidden; }
  body {
    font-family: "Open Sans", Arial, sans-serif;
    background: var(--backdrop);
    position: relative;
  }
  .logo-strip {
    position: absolute; left: 0; top: 0;
    width: 1200px; height: 250px;
    background: var(--paper);
    display: flex; align-items: center; justify-content: center;
  }
  .brand {
    display: flex; flex-direction: column; align-items: center; gap: 8px;
  }
  .brand-row { display: flex; align-items: center; gap: 14px; }
  .brand-dot {
    border-radius: 50%;
    background: var(--ink);
    flex: none;
  }
  .brand-name {
    font-weight: 800;
    color: var(--ink);
    letter-spacing: 0.5px;
    line-height: 1;
    white-space: nowrap;
  }
  .brand-tagline {
    font-weight: 600;
    color: var(--ink);
    line-height: 1.2;
    white-space: nowrap;
  }
  .brand--large .brand-dot { width: 64px; height: 64px; }
  .brand--large .brand-name { font-size: 40px; }
  .brand--large .brand-tagline { font-size: 12px; }

  .brand--card .brand-dot { width: 46px; height: 46px; }
  .brand--card .brand-name { font-size: 28px; }
  .brand--card .brand-tagline { font-size: 9px; }

  .card {
    position: absolute;
    top: 440px;
    width: 540px; height: 300px;
    background: var(--paper);
    overflow: hidden;
    box-shadow: 0 6px 18px rgba(0,0,0,0.18);
  }
  .card--front { left: 40px; display: flex; align-items: center; justify-content: center; }
  .card--back { left: 620px; }

  .card--back .brand {
    position: absolute; left: 20px; top: 122px;
    align-items: center;
    gap: 6px;
  }
  .card--back .brand-row { gap: 10px; }
  .card--back .brand--card .brand-name { font-size: 18px; }
  .card--back .brand--card .brand-dot { width: 32px; height: 32px; }
  .card--back .brand--card .brand-tagline { font-size: 7px; }

  .panel-arc {
    position: absolute; border-radius: 50%;
    width: 560px; height: 560px;
  }
  .panel-arc--accent { left: 264px; top: -118px; background: var(--orange); }
  .panel-arc--dark {
    left: 280px; top: -132px;
    background: linear-gradient(120deg, var(--charcoal) 0%, var(--charcoal-light) 100%);
  }
  .contact {
    position: absolute; left: 336px; top: 96px;
    color: var(--paper);
  }
  .contact-name { color: var(--orange); font-size: 17px; font-weight: 400; line-height: 1.2; }
  .contact-title { font-size: 14px; line-height: 1.3; margin-bottom: 16px; }
  .contact-list { list-style: none; font-size: 12px; line-height: 1.55; white-space: nowrap; }
  .contact-label { color: var(--orange); display: inline-block; width: 18px; }
</style>
</head>
<body>
  <header class="logo-strip">
    <div class="brand brand--large">
      <div class="brand-row">
        <span class="brand-dot"></span>
        <span class="brand-name">FixyNestly.com</span>
      </div>
      <p class="brand-tagline">We Tackle The Chore Lists That Other Crews Skip Past!</p>
    </div>
  </header>

  <section class="card card--front">
    <div class="brand brand--card">
      <div class="brand-row">
        <span class="brand-dot"></span>
        <span class="brand-name">FixyNestly.com</span>
      </div>
      <p class="brand-tagline">We Tackle The Chore Lists That Other Crews Skip Past!</p>
    </div>
  </section>

  <section class="card card--back">
    <div class="brand brand--card">
      <div class="brand-row">
        <span class="brand-dot"></span>
        <span class="brand-name">FixyNestly.com</span>
      </div>
      <p class="brand-tagline">We Tackle The Chore Lists That Other Crews Skip Past!</p>
    </div>
    <div class="panel-arc panel-arc--accent"></div>
    <div class="panel-arc panel-arc--dark"></div>
    <div class="contact">
      <p class="contact-name">Your Name</p>
      <p class="contact-title">Title</p>
      <ul class="contact-list">
        <li><span class="contact-label">m:</span>(XXX) 1234 567</li>
        <li><span class="contact-label">p:</span>(XXX) 1234568</li>
        <li><span class="contact-label">e:</span>name@domain.com</li>
      </ul>
    </div>
  </section>
</body>
</html>
```